PDBA website design

We need a page template website design for a cms website. Please see the brief attached for the details.
The client is the Pacific Downhorn Breeders Association which is an organisation promoting the White Suffolk Sheep Breed within Australia.

Reason: So that my top few designs can make changes and re-submit.

Target Market(s)

See attached brief

```html
<!DOCTYPE html>
<html lang="en">
<head>
<meta charset="utf-8">
<title>Pacific Downhorn Breeders Association</title>
<link href="https://fonts.googleapis.com/css2?family=Lato:wght@300;400;700;900&display=swap" rel="stylesheet">
<style>
:root{
  --green:#1a8a3c;
  --green-dark:#0f6b2a;
  --nav-dark:#2b2b2b;
  --yellow:#efe01e;
  --ring:#e8e02a;
  --ink:#222;
  --text:#333;
  --panel:#f3f3f3;
  --footer:#262626;
  --footer-top:#555;
  --footer-text:#d8d8d8;
  --sponsor-red:#e0462a;
}
*{box-sizing:border-box;margin:0;padding:0}
html,body{width:1120px;height:1200px;overflow:hidden;background:#fff;font-family:'Lato',sans-serif;color:var(--text)}
.site{position:relative;width:1120px;height:1200px}
.hero{position:absolute;left:0;top:0;width:1120px;height:319px;
  background:linear-gradient(180deg,#7b6a56 0%,#8a7a62 30%,#b59a72 55%,#c9a878 80%,#b08d62 100%)}
.masthead{position:absolute;left:170px;top:8px;width:781px;height:93px;background:#f1f1f1;display:flex;align-items:center}
.brand{width:190px;padding-left:22px;display:flex;align-items:center;gap:8px;font-weight:900;font-size:24px;color:var(--green)}
.brand-dot{width:16px;height:16px;border-radius:50%;background:var(--green)}
.site-title{font-size:35px;font-weight:700;color:var(--ink);letter-spacing:-.2px;margin-left:12px}
.main-nav{position:absolute;left:170px;top:101px;width:781px;height:43px;display:flex;background:var(--green-dark)}
.main-nav a{display:flex;align-items:center;justify-content:center;color:#fff;text-decoration:none;font-weight:700;font-size:12.5px;border-right:1px solid #0a5220}
.main-nav a.active{background:var(--nav-dark)}
.main-nav a:last-child{border-right:0}
.sidebar{position:absolute;left:169px;top:358px;width:227px}
.quick-link{height:104px;background:var(--panel);border:1px solid #d6d6d6;border-radius:2px;box-shadow:0 2px 2px rgba(0,0,0,.12);margin-bottom:9px;display:flex;align-items:center;padding-left:16px}
.icon-ring{width:70px;height:70px;border-radius:50%;background:var(--ring);padding:3px;flex:none;box-shadow:2px 3px 4px rgba(0,0,0,.25)}
.icon-ring span{display:flex;width:100%;height:100%;border-radius:50%;background:#4a4a4a;align-items:center;justify-content:center}
.quick-label{margin-left:10px;font-size:15px;font-weight:700;color:var(--ink);line-height:19px;text-transform:uppercase}
.quick-label small{display:block;font-size:11px;color:var(--green);line-height:19px}
.sponsor-head{height:34px;background:var(--yellow);border-radius:2px;font-weight:700;font-size:15px;color:var(--ink);padding:8px 11px;margin-top:3px}
.sponsor-ad{margin:6px 2px 0;width:224px;height:174px;background:var(--sponsor-red);position:relative}
.sponsor-name{position:absolute;left:20px;top:5px;color:#fff;font-size:17px;font-weight:700;line-height:19px}
.sponsor-photo{position:absolute;left:0;top:45px;width:224px;height:105px;background:linear-gradient(180deg,#8a8560 0%,#7a5a3a 50%,#6b7a48 100%)}
.sponsor-url{position:absolute;left:0;bottom:2px;width:224px;text-align:center;color:#fff;font-size:13px;font-weight:700}
.view-all{display:block;margin:10px 0 0 3px;color:var(--green);font-size:11px;font-weight:700;text-decoration:none}
.content{position:absolute;left:413px;top:356px;width:535px;font-size:12px;line-height:21px}
.welcome{font-weight:300;font-size:29px;line-height:31px;color:var(--ink)}
.welcome strong{display:block;font-weight:700;color:var(--green);font-size:29px;line-height:33px}
.content p{margin-top:4px}
.content a{color:var(--green)}
.content h2{font-size:14px;font-weight:700;color:var(--green);margin-top:21px;line-height:22px}
.checklist{list-style:none;margin-top:1px}
.checklist li{display:flex;align-items:center;gap:6px;line-height:23px}
.footer{position:absolute;left:0;top:1076px;width:1120px;height:124px;background:var(--footer);border-top:6px solid var(--footer-top);color:var(--footer-text);font-size:11px}
.copyright{position:absolute;left:170px;top:28px;line-height:21px}
.copyright a{color:var(--green);text-decoration:none}
.follow{position:absolute;left:494px;top:24px;display:flex;align-items:center;gap:10px}
.social-box{width:21px;height:21px;border-radius:2px;background:#3b5a98}
.contact-list{position:absolute;left:698px;top:24px;line-height:21px}
.contact-list div{display:flex}
.contact-list dt{width:58px}
.contact-list .sep{width:28px}
</style>
</head>
<body>
<div class="site">
  <div class="hero" role="img" aria-label="Photograph of a flock of white-faced sheep standing in a paddock"></div>

  <header class="masthead">
    <div class="brand"><span class="brand-dot"></span>PDBA</div>
    <h1 class="site-title">Pacific Downhorn Breeders Association</h1>
  </header>

  <nav class="main-nav">
    <a class="active" href="#" style="width:73px">HOME</a>
    <a href="#" style="width:75px">ABOUT</a>
    <a href="#" style="width:83px">SEARCH</a>
    <a href="#" style="width:148px">MEMBER SERVICES</a>
    <a href="#" style="width:107px">STUD PAGES</a>
    <a href="#" style="width:70px">NEWS</a>
    <a href="#" style="width:66px">SALES</a>
    <a href="#" style="width:68px">LINKS</a>
    <a href="#" style="width:91px">CONTACT</a>
  </nav>

  <aside class="sidebar">
    <a class="quick-link" href="#" style="text-decoration:none">
      <div class="icon-ring"><span>
        <svg width="34" height="34" viewBox="0 0 24 24"><path fill="#fff" d="M6.6 10.8a15 15 0 0 0 6.6 6.6l2.2-2.2c.3-.3.7-.4 1-.2 1.1.4 2.3.6 3.6.6.6 0 1 .4 1 1V20c0 .6-.4 1-1 1A17 17 0 0 1 3 4c0-.6.4-1 1-1h3.5c.6 0 1 .4 1 1 0 1.3.2 2.5.6 3.6.1.3 0 .7-.2 1z"/></svg>
      </span></div>
      <div class="quick-label">Prime Lamb<br>Helpline</div>
    </a>
    <a class="quick-link" href="#" style="text-decoration:none">
      <div class="icon-ring"><span>
        <svg width="38" height="38" viewBox="0 0 24 24" fill="none" stroke="#fff" stroke-width="1.6"><rect x="3" y="5" width="18" height="16" rx="1.5"/><path d="M3 9h18M8 3v4M16 3v4M7 13h2M11 13h2M15 13h2M7 17h2M11 17h2M15 17h2"/></svg>
      </span></div>
      <div class="quick-label">Events</div>
    </a>
    <a class="quick-link" href="#" style="text-decoration:none">
      <div class="icon-ring"><span>
        <svg width="44" height="36" viewBox="0 0 30 24"><circle cx="11" cy="7" r="5" fill="#fff"/><path d="M1 22c0-6 4-9 10-9s10 3 10 9z" fill="#fff"/><circle cx="21" cy="9" r="4" fill="#fff"/><path d="M17 22c0-5 2-8 6-8s6 3 6 8z" fill="#fff"/></svg>
      </span></div>
      <div class="quick-label">Members<small>Members Resources</small><small>Webmanager Login</small></div>
    </a>
    <a class="quick-link" href="#" style="text-decoration:none">
      <div class="icon-ring"><span>
        <svg width="38" height="38" viewBox="0 0 24 24" fill="none" stroke="#fff" stroke-width="1.8" stroke-linejoin="round"><path d="M3 10h4l10-5v14L7 14H3z"/><path d="M6 14l2 6h2l-1-6"/><path d="M20 9v6"/></svg>
      </span></div>
      <div class="quick-label">Latest<br>News</div>
    </a>
    <div class="sponsor-head">SPONSORS</div>
    <div class="sponsor-ad">
      <div class="sponsor-name">Paddock Market<br>Stock</div>
      <div class="sponsor-photo" role="img" aria-label="Photograph of two cattle grazing in a field"></div>
      <div class="sponsor-url">www.paddockmarketstock.com.au</div>
    </div>
    <a class="view-all" href="#">VIEW ALL SPONSORS&gt;</a>
  </aside>

  <main class="content">
    <h2 class="welcome" style="margin-top:0;font-size:29px;font-weight:300;color:var(--ink);line-height:31px">WELCOME TO<strong>Pacific Downhorn Breeders Association</strong></h2>
    <p>Lorem ipsum dolor sit amet, consectetur adipiscing elit. Sed quis nisi euismod, fermentum tellus a, lobortis quam. <b>Vestibulum condimentum</b> mi vitae diam tristique, egestas dignissim diam mattis. <a href="#">Curabitur vel diam</a> in massa porttitor dictum id in lorem.</p>
    <h2>Vivamus faucibus ac leo ac dignissim.</h2>
    <p style="margin-top:0">Maecenas orci est, euismod facilisis feugiat sit amet, semper ut tortor. Donec eleifend accumsan nisl, nec laoreet leo iaculis sit amet. Vivamus varius arcu eu sagittis aliquam. Vivamus accumsan cursus hendrerit. <b>Vivamus eu magna rhoncus</b>, consectetur metus ac, varius lacus.</p>
    <h2>Donec ultricies, tortor quis sagittis sagittis</h2>
    <ul class="checklist">
      <li><svg width="11" height="9" viewBox="0 0 12 10"><path d="M1 5l3.5 3.5L11 1.5" fill="none" stroke="#1a8a3c" stroke-width="2.6"/></svg>Mauris erat ullamcorper augue, eu placerat diam nunc a lorem.</li>
      <li><svg width="11" height="9" viewBox="0 0 12 10"><path d="M1 5l3.5 3.5L11 1.5" fill="none" stroke="#1a8a3c" stroke-width="2.6"/></svg>Nam vulputate mauris id arcu pharetra, sed posuere quam cursus.</li>
      <li><svg width="11" height="9" viewBox="0 0 12 10"><path d="M1 5l3.5 3.5L11 1.5" fill="none" stroke="#1a8a3c" stroke-width="2.6"/></svg>Nullam eget massa vel mi posuere venenatis sed quis tortor.</li>
      <li><svg width="11" height="9" viewBox="0 0 12 10"><path d="M1 5l3.5 3.5L11 1.5" fill="none" stroke="#1a8a3c" stroke-width="2.6"/></svg>In hac habitasse platea dictumst. Fusce nisi tellus, fermentum a luctus eget, convallis.</li>
      <li><svg width="11" height="9" viewBox="0 0 12 10"><path d="M1 5l3.5 3.5L11 1.5" fill="none" stroke="#1a8a3c" stroke-width="2.6"/></svg>In commodo egestas magna quis placerat. Quisque adipiscing consequat nisi.</li>
    </ul>
    <h2>Cras accumsan orci mauris ut aliquam ipsum faucibus sed.</h2>
    <p style="margin-top:0">Fusce quam dui, accumsan a magna in, faucibus tristique lectus. Vestibulum sapien leo, placerat quis luctus eget, auctor et justo. Vestibulum ante ipsum primis in faucibus orci luctus et ultrices posuere cubilia Curae; <b>Duis sagittis</b>, risus ut viverra dignissim, lectus nunc iaculis arcu, et gravida est tortor ut erat. Morbi a feugiat dolor, in tristique elit. Mauris feugiat aliquam vulputate. Etiam sed mi quis velit commodo mollis et eu quam. Vestibulum mollis at dolor sed egestas.</p>
    <h2>Vivamus faucibus ac leo ac dignissim.</h2>
    <p style="margin-top:0">Maecenas orci est, euismod facilisis feugiat sit amet, semper ut tortor. Donec eleifend accumsan nisl, nec laoreet leo iaculis sit amet. Vivamus varius arcu eu sagittis aliquam. Vivamus accumsan cursus hendrerit. Vivamus eu magna rhoncus, consectetur metus ac, varius lacus.</p>
  </main>

  <footer class="footer">
    <div class="copyright">Copyright Pacific Downhorn Breeders Association<br><a href="#">Website design and development by Fieldline Studio</a></div>
    <div class="follow">Follow us on: <span class="social-box"></span></div>
    <dl class="contact-list">
      <div><dt>Address</dt><span class="sep">:</span><dd>PO Box 412, Greenvale, SA 5099</dd></div>
      <div><dt>Phone</dt><span class="sep">:</span><dd>08 7000 1234</dd></div>
      <div><dt>Fax</dt><span class="sep">:</span><dd>08 7000 1235</dd></div>
      <div><dt>Email</dt><span class="sep">:</span><dd>info@downhornbreeders.org</dd></div>
    </dl>
  </footer>
</div>
</body>
</html>
```